Cover for a Non-Fiction Book on Authoritarianism for a Washington D.C. Think Tank

Create a dynamic and engaging cover highlighting the role of contemporary and historical authoritarianism for a non-fiction edited volume. The book brings together chapters from many leading academics on the subject. The tone should be serious but provocative. Proprietary images are not acceptable as we are not budgeting for licensing. The books dimensions are 6x9. Preference will be given to designers with front and back cover design with sample ipsum lorum text.

One of covers that we particularly liked was "How Quiet Defiance Endures" a link to the image on shelvoria is: http://www.shelvoria-books.example/s/ref=nb_sb_noss/482-7715093-6620841?url=search-alias%3Daps&field-keywords=How+Quiet+Defiance+Endures

Attached is a draft version of the manuscript to assist in shaping your creative vision.

Project Deadline Extended Reason: I have extended the deadline at the request of the editors. They would like to see some designs that rely less heavily on the themes of fists and barbed wire to reference authoritarianism. I apologize to designs with current submissions, some of them are very professional, however none of the designs are currently under consideration for use. Added Saturday, January 24, 2015

Project Deadline Extended Reason: Editors are still unsatisfied with current sample of options. I apologize to those current contributors, but anything challenging and new would be well received. Added Friday, January 30, 2015

Project Deadline Extended Reason: I've updated the deadline so that designers that were well ranked can submit full front and back covers to assist the book editors in making their final decision. Added Friday, February 13, 2015

Font styles to use
Serif
Sans Serif

Requirements
Must have
• 1) Title: Are Strongmen Regaining the Upper Ground
• 2) Editors: Tobias Lindqvern and Elena K. Marwood
• 3) Language from client: "a simple design that captured both a symbol of repression and resistance would be ideal. The cover of How Quiet Defiance Endures is a great example. Nothing busy or overly complicated. The image of mass street protests may be overused at this point so I'd opt for something a bit more creative. Vibrant colors always great."
• 4) This final project design must use the attached InDesign template file when constructing the cover (IDML and INDD versions of the template are available).
Nice to have
• Feel free to use Harborline Forum logo designs pulled from the web.
Should not have
• Photographs that would require compensating a copyright holder.

```html
<!DOCTYPE html>
<html lang="en">
<head>
<meta charset="utf-8">
<title>Are Strongmen Regaining the Upper Ground? — Book Cover</title>
<link rel="stylesheet" href="https://fonts.googleapis.com/css2?family=Montserrat:wght@700;800&family=Open+Sans:wght@300&display=swap">
<style>
  :root {
    --band-grey: #b3b3b3;
    --ink: #1a1a1a;
    --cover-red: #f5160c;
    --cover-red-light: #ff3a22;
    --cover-red-deep: #d90f08;
    --redaction: #0d0d0d;
    --paper: #ffffff;
    --publisher-blue: #1d3fe0;
  }
  * { margin: 0; padding: 0; box-sizing: border-box; }
  html, body { width: 847px; height: 1200px; overflow: hidden; background: var(--paper); }
  .cover { position: relative; width: 847px; height: 1200px; }
  .editors-band {
    position: absolute; left: 0; top: 0; width: 847px; height: 212px;
    background: var(--band-grey);
    display: flex; align-items: center; justify-content: center;
    padding-bottom: 14px;
  }
  .editors {
    font-family: "Open Sans", sans-serif; font-weight: 300;
    font-size: 39px; color: var(--ink); letter-spacing: -0.3px;
  }
  .title-panel {
    position: absolute; left: 0; top: 212px; width: 847px; height: 836px;
    background: radial-gradient(ellipse at 50% 48%, var(--cover-red-light) 0%, var(--cover-red) 45%, var(--cover-red-deep) 100%);
    overflow: hidden;
  }
  .world-map {
    position: absolute; left: 0; top: 30px; width: 847px; height: 760px;
    background: radial-gradient(ellipse at 55% 40%, rgba(255,170,160,0.28) 0%, rgba(255,120,110,0.12) 50%, rgba(120,0,0,0.1) 100%);
  }
  .title-art { position: absolute; left: 0; top: 0; }
  .title-dark { font-family: "Montserrat", sans-serif; font-weight: 800; fill: var(--redaction); }
  .title-light { font-family: "Montserrat", sans-serif; font-weight: 800; fill: var(--paper); }
  .redaction-bar { fill: var(--redaction); }
  .publisher-band {
    position: absolute; left: 0; top: 1048px; width: 847px; height: 152px;
    background: var(--paper);
    display: flex; align-items: center; justify-content: center; gap: 12px;
    padding-bottom: 6px;
  }
  .publisher-mark {
    width: 38px; height: 38px; border-radius: 50%; background: var(--publisher-blue);
  }
  .publisher-name {
    font-family: "Montserrat", sans-serif; font-weight: 700;
    font-size: 36px; color: var(--publisher-blue);
  }
</style>
</head>
<body>
<div class="cover">
  <header class="editors-band">
    <p class="editors">Tobias Lindqvern and Elena K. Marwood</p>
  </header>

  <section class="title-panel">
    <div class="world-map" role="img" aria-label="Dotted world map in light red tones across the panel"></div>
    <svg class="title-art" width="847" height="836" viewBox="0 212 847 836" aria-labelledby="book-title">
      <title id="book-title">Are Strongmen Regaining the Upper Ground?</title>
      <g transform="rotate(-17 430 640)">
        <!-- redaction bars -->
        <rect class="redaction-bar" x="-60" y="530" width="200" height="30"/>
        <rect class="redaction-bar" x="268" y="522" width="240" height="34"/>
        <rect class="redaction-bar" x="540" y="518" width="420" height="34"/>
        <rect class="redaction-bar" x="-80" y="612" width="150" height="32"/>
        <rect class="redaction-bar" x="110" y="612" width="110" height="28"/>
        <rect class="redaction-bar" x="-60" y="660" width="300" height="34"/>
        <rect class="redaction-bar" x="290" y="628" width="250" height="30"/>
        <rect class="redaction-bar" x="600" y="626" width="320" height="30"/>
        <rect class="redaction-bar" x="260" y="665" width="60" height="24"/>
        <rect class="redaction-bar" x="350" y="664" width="80" height="26"/>
        <rect class="redaction-bar" x="460" y="668" width="220" height="26"/>
        <rect class="redaction-bar" x="720" y="660" width="160" height="26"/>
        <!-- title -->
        <text class="title-dark" x="160" y="560" font-size="52">ARE</text>
        <text class="title-dark" x="234" y="610" font-size="62" textLength="606" lengthAdjust="spacingAndGlyphs">STRONGMEN</text>
        <text class="title-light" x="14" y="727" font-size="48" textLength="750" lengthAdjust="spacingAndGlyphs">REGAINING THE UPPER GROUND?</text>
      </g>
    </svg>
  </section>

  <footer class="publisher-band">
    <span class="publisher-mark" aria-hidden="true"></span>
    <span class="publisher-name">Harborline Forum</span>
  </footer>
</div>
</body>
</html>
```